Amber Lantern Cafe Business Card

We need a business card design for a new European Cafe. Main menu will be coffee and deserts.

Requirements
Must have
• Logo - 1 of the attached versions
Address - TBA (you can use 487 Morrow Ave Unit 9 for now)
Phone - TBA (you can use 555-238-4176 for now)

```html
<!DOCTYPE html>
<html lang="en">
<head>
<meta charset="utf-8">
<title>Amber Lantern Cafe – Business Card</title>
<link rel="stylesheet" href="https://fonts.googleapis.com/css2?family=Open+Sans:wght@400;600&display=swap">
<style>
  :root {
    --brand-red: #e0202a;
    --card-white: #ffffff;
    --text-grey: #a9a9a9;
    --page-bg: #ecebea;
    --card-shadow: rgba(0, 0, 0, 0.18);
  }
  * { box-sizing: border-box; margin: 0; padding: 0; }
  html, body {
    width: 1200px;
    height: 1000px;
    overflow: hidden;
    background: var(--page-bg);
    font-family: "Open Sans", sans-serif;
  }
  .sheet { position: relative; width: 1200px; height: 1000px; }
  .card {
    position: absolute;
    left: 250px;
    width: 700px;
    height: 400px;
    background: var(--card-white);
    box-shadow: 0 6px 20px var(--card-shadow);
    overflow: hidden;
  }
  .card--front { top: 60px; }
  .card--back { top: 530px; }

  /* Front */
  .front-lockup {
    position: absolute;
    inset: 0;
    display: flex;
    flex-direction: column;
    align-items: center;
    justify-content: center;
  }
  .brand-square {
    width: 150px;
    height: 150px;
    background: var(--brand-red);
    border-radius: 10px;
    margin-bottom: 26px;
  }
  .brand-name {
    color: var(--brand-red);
    font-weight: 600;
    text-align: center;
    line-height: 1.08;
  }
  .brand-name__line { display: block; }
  .front-lockup .brand-name__line--main { font-size: 48px; }
  .front-lockup .brand-name__line--sub { font-size: 38px; letter-spacing: 2px; }

  /* Back */
  .back-square {
    position: absolute;
    right: -40px;
    top: 40px;
    width: 290px;
    height: 290px;
    background: var(--brand-red);
    border-radius: 16px;
    transform: rotate(14deg);
  }
  .contact {
    position: absolute;
    left: 48px;
    top: 112px;
  }
  .contact .brand-name {
    text-align: left;
    margin-bottom: 26px;
  }
  .contact .brand-name__line--main { font-size: 30px; }
  .contact .brand-name__line--sub { font-size: 24px; letter-spacing: 1px; }
  .contact__row {
    display: flex;
    align-items: center;
    gap: 12px;
    font-size: 22px;
    line-height: 1;
    margin-bottom: 16px;
  }
  .contact__row--address { color: var(--text-grey); }
  .contact__row--phone { color: var(--brand-red); }
  .contact__icon { width: 20px; height: 22px; flex: none; }
</style>
</head>
<body>
<main class="sheet">

  <section class="card card--front" aria-label="Card front">
    <div class="front-lockup">
      <div class="brand-square"></div>
      <div class="brand-name">
        <span class="brand-name__line brand-name__line--main">Amber Lantern</span>
        <span class="brand-name__line brand-name__line--sub">Cafe</span>
      </div>
    </div>
  </section>

  <section class="card card--back" aria-label="Card back">
    <div class="back-square"></div>
    <div class="contact">
      <div class="brand-name">
        <span class="brand-name__line brand-name__line--main">Amber Lantern</span>
        <span class="brand-name__line brand-name__line--sub">Cafe</span>
      </div>
      <div class="contact__row contact__row--address">
        <svg class="contact__icon" viewBox="0 0 20 22" aria-hidden="true">
          <path d="M10 1a7 7 0 0 0-7 7c0 5 7 13 7 13s7-8 7-13a7 7 0 0 0-7-7z" fill="var(--text-grey)"/>
          <circle cx="10" cy="8" r="2.6" fill="var(--card-white)"/>
        </svg>
        <span>487 Morrow Ave Unit 9</span>
      </div>
      <div class="contact__row contact__row--phone">
        <svg class="contact__icon" viewBox="0 0 20 22" aria-hidden="true">
          <path d="M1 8c0-3 4-4 9-4s9 1 9 4v2h-4V8H5v2H1z" fill="var(--brand-red)"/>
          <path d="M4 11h12l2 8H2z" fill="var(--brand-red)"/>
          <circle cx="10" cy="15" r="2.2" fill="var(--card-white)"/>
        </svg>
        <span>555-238-4176</span>
      </div>
    </div>
  </section>

</main>
</body>
</html>
```